Business Card Design for Fashion Tech Startup

Dear designers, we need a business card for Asia's premier fashion tech startup.!

PebbleHop is discovery e-commerce destination for busy, discerning parents in Asia featuring leading independent designers of baby, kids fashion apparel and sustainable brands from around the world.

PebbleHop is a modern, contemporary fashion tech startup targeting well-educated, well travelled and affluent parents. We're NOT your typical kiddy store!! Our design philosophy & e-commerce site is more like Vask.com, Orimesa.com, Pondwick.com, Farthollow.com.
Updates

Hi, size of the business card should be 84mm X 55mm. Would appreciate some business card layouts in Portrait as added consideration, i fancy the idea of a Portrait business card. What's important is that the business card should pique the receiver's interest to log onto the website to learn more. Many thanks and love forward to the designs!

Target Market(s)

Though modern, classy in look, feel & positioning, PebbleHop does possess a cheeky, fun-loving personality as depicted by its logo and the segment it targets (baby, kids) though the key decision makers i.e primarily mums between 25-40 who are well educated/travelled, local & expatriates, internet/digitally savvy, mid-high income working mums.

Industry/Entity Type

E-Commerce

Requirements
Must have
• Name, designation, email, phone & mobile number.
Company url : www.pebblehop.sg
Slogan : Discovery e-commerce destination for discerning, busy parents
Nice to have
• Call to Action such as a Discount code offering 10% discount
or asking people to "Like" us on our Chatterly page/Chatterly URL

```html
<!DOCTYPE html>
<html lang="en">
<head>
<meta charset="utf-8">
<title>PebbleHop Business Card</title>
<link rel="stylesheet" href="https://fonts.googleapis.com/css2?family=Josefin+Sans:wght@300;400;700&family=Archivo+Narrow:wght@400;600&display=swap">
<style>
  :root {
    --backdrop: #2b2b2c;
    --card-white: #ffffff;
    --card-mist: #f2f4f6;
    --teal: #3b5e72;
    --teal-pale: #9fb3bf;
    --coral: #f06b57;
    --ink: #5d6c76;
    --rule: #b9c4cb;
  }
  * { box-sizing: border-box; margin: 0; padding: 0; }
  html, body { width: 1200px; height: 900px; overflow: hidden; }
  body {
    background: var(--backdrop);
    font-family: "Josefin Sans", sans-serif;
    display: flex; align-items: center; justify-content: center; gap: 80px;
  }
  .card {
    position: relative;
    width: 406px; height: 620px;
    border-radius: 34px;
    background: var(--card-white);
    padding: 12px;
    overflow: hidden;
  }
  .card-inner {
    position: relative; width: 100%; height: 100%;
    border-radius: 24px; overflow: hidden;
    background: var(--card-mist);
  }

  /* Front */
  .top-band { height: 34px; background: var(--teal); border-bottom: 4px solid var(--rule); }
  .brand { display: flex; align-items: center; gap: 14px; padding: 34px 0 0 34px; }
  .brand-dot { width: 62px; height: 62px; border-radius: 50%; background: var(--coral); flex: none; }
  .brand-name { font-weight: 700; font-size: 36px; color: var(--coral); letter-spacing: 0.5px; }
  .role-row { display: flex; align-items: center; gap: 10px; margin: 40px 28px 0 28px; }
  .role-row .line { flex: 1; height: 1px; background: var(--rule); }
  .role { font-weight: 300; font-size: 19px; color: var(--ink); letter-spacing: 2px; }
  .person { font-weight: 300; font-size: 44px; color: var(--teal); letter-spacing: 3px; text-align: center; margin-top: 8px; white-space: nowrap; }
  .rule { height: 1px; background: var(--rule); margin: 8px 18px; }
  .contact { font-family: "Archivo Narrow", sans-serif; font-size: 15.5px; color: var(--ink); line-height: 1.45; padding: 6px 34px; }
  .url { font-family: "Archivo Narrow", sans-serif; font-size: 14px; letter-spacing: 6px; color: var(--ink); padding: 10px 34px; }
  .meadow-front {
    position: absolute; left: 0; right: 0; bottom: 0; height: 200px;
    background: linear-gradient(to bottom, rgba(59,94,114,0) 0%, rgba(59,94,114,0.55) 30%, var(--teal) 62%);
  }
  .cta {
    position: absolute; left: 0; right: 0; bottom: 26px;
    text-align: center; color: #ffffff;
    font-family: "Archivo Narrow", sans-serif; font-weight: 600; font-size: 19px; letter-spacing: 0.5px;
  }

  /* Back */
  .back .card-inner { background: var(--teal); }
  .back-strip { height: 22px; background: var(--card-white); border-bottom: 3px solid var(--teal-pale); }
  .back-brand { display: flex; align-items: center; justify-content: center; gap: 14px; margin-top: 150px; }
  .back-brand .brand-dot { background: var(--card-white); width: 56px; height: 56px; }
  .back-brand .brand-name { color: var(--card-white); font-size: 32px; }
  .slogan {
    margin: 16px 40px 0; text-align: center; color: var(--card-mist);
    font-family: "Archivo Narrow", sans-serif; font-size: 14px; line-height: 1.4; letter-spacing: 0.5px;
  }
  .meadow-back {
    position: absolute; left: 0; right: 0; top: 340px; height: 150px;
    background: linear-gradient(to bottom, rgba(255,255,255,0) 0%, rgba(255,255,255,0.45) 55%, var(--card-white) 100%);
  }
  .back-foot {
    position: absolute; left: 0; right: 0; bottom: 0; height: 106px;
    background: var(--card-white);
    display: flex; align-items: center; justify-content: center;
  }
  .back-foot .url { color: var(--ink); padding: 0; }
</style>
</head>
<body>
  <section class="card front">
    <div class="card-inner">
      <div class="top-band"></div>
      <div class="brand">
        <span class="brand-dot"></span>
        <span class="brand-name">PebbleHop</span>
      </div>
      <div class="role-row"><span class="line"></span><span class="role">President</span><span class="line"></span></div>
      <h1 class="person">OWEN BLAKE</h1>
      <div class="rule"></div>
      <p class="contact">Po box 214 Linden Rd, Harbour Point<br>065-481-2207 &bull; owen@pebblehop.sg</p>
      <div class="rule"></div>
      <p class="url">www.pebblehop.sg</p>
      <div class="meadow-front" role="img" aria-label="Silhouette of wild grasses and flowers"></div>
      <p class="cta">&ldquo;Like&rdquo; us on our Chatterly</p>
    </div>
  </section>

  <section class="card back">
    <div class="card-inner">
      <div class="back-strip"></div>
      <div class="back-brand">
        <span class="brand-dot"></span>
        <span class="brand-name">PebbleHop</span>
      </div>
      <p class="slogan">Discovery e-commerce destination for discerning, busy parents</p>
      <div class="meadow-back" role="img" aria-label="White silhouette of wild grasses and flowers"></div>
      <div class="back-foot"><p class="url">www.pebblehop.sg</p></div>
    </div>
  </section>
</body>
</html>
```